We want a business card/punch card for our business. We are including examples of our current business card (we like the front of our business card and not looking to remake it). We need only back side to be designed in form of a punch card (we are including a sample of the punch card we made, but are unsatisfied). For each $180 spend (9 punches) our clients have $20 off.

Colors
886aae

```html
<!DOCTYPE html>
<html lang="en">
<head>
<meta charset="utf-8">
<title>Lunar Path Studio – Business Card &amp; Punch Card</title>
<link href="https://fonts.googleapis.com/css2?family=Cinzel:wght@400;600&family=Lato:wght@400;700&display=swap" rel="stylesheet">
<style>
  :root {
    --backdrop: #3b3b3b;
    --card: #050505;
    --periwinkle: #5a67b9;
    --violet: #6b3fa0;
    --ink: #ffffff;
    --cream: #e8dcc0;
  }
  * { box-sizing: border-box; margin: 0; padding: 0; }
  html, body {
    width: 1200px; height: 1200px; overflow: hidden;
    background: var(--backdrop);
    font-family: "Lato", sans-serif;
    color: var(--ink);
  }
  .card {
    position: absolute;
    top: 162px;
    width: 466px; height: 814px;
    background: var(--card);
  }
  .card--front { left: 76px; }
  .card--back { left: 658px; }

  /* Front */
  .brand-mark {
    position: absolute; left: 173px; top: 60px;
    width: 120px; height: 120px; border-radius: 50%;
    background: var(--violet);
  }
  .brand-name {
    position: absolute; left: 0; width: 100%;
    text-align: center;
    font-family: "Cinzel", serif; font-weight: 600;
    color: var(--periwinkle);
    line-height: 1.1;
  }
  .card--front .brand-name { top: 262px; font-size: 44px; }
  .holder-name {
    position: absolute; left: 0; top: 464px; width: 100%;
    text-align: center;
    font-family: "Cinzel", serif; font-weight: 400;
    font-size: 30px; color: var(--periwinkle);
    letter-spacing: 0.5px;
  }
  .contact-icons {
    position: absolute; left: 0; top: 559px; width: 100%;
    display: flex; justify-content: center; gap: 12px;
  }
  .contact-icons svg { width: 17px; height: 17px; }
  .contact-list {
    position: absolute; left: 0; top: 586px; width: 100%;
    text-align: center; font-size: 24px; line-height: 30px;
  }
  .social-list {
    position: absolute; left: 0; top: 738px; width: 100%;
    text-align: center; font-size: 17px; line-height: 21px;
  }

  /* Back */
  .card--back .brand-name { top: 72px; font-size: 50px; }
  .services {
    position: absolute; left: 0; top: 280px; width: 100%;
    text-align: center; font-size: 19px; line-height: 28px;
  }
  .services .row { display: block; }
  .services .row--ruled span { border-bottom: 1.5px solid var(--periwinkle); padding: 0 2px 1px; }
  .dot {
    display: inline-block; width: 11px; height: 11px; border-radius: 50%;
    background: var(--periwinkle); border: 1.5px solid #9aa4e0;
    margin: 0 6px; vertical-align: 0;
  }
  .punch-grid {
    position: absolute; left: 40px; top: 454px;
    display: grid; grid-template-columns: repeat(3, 108px);
    column-gap: 25px; row-gap: 10px;
  }
  .punch {
    position: relative; width: 108px; height: 108px;
  }
  .punch svg { position: absolute; inset: 0; }
  .punch__value {
    position: absolute; inset: 0;
    display: flex; align-items: center; justify-content: center;
    font-size: 23px; font-weight: 700; color: var(--ink);
  }
</style>
</head>
<body>

<section class="card card--front">
  <div class="brand-mark"></div>
  <div class="brand-name">Lunar Path<br>Studio</div>
  <div class="holder-name">SELENE MARLOWE</div>

  <div class="contact-icons">
    <svg viewBox="0 0 20 20" aria-label="phone"><path d="M5 2l3 4-2 2c1 2 3 4 5 5l2-2 4 3-2 3C9 17 3 11 2 5z" fill="var(--periwinkle)"/></svg>
    <svg viewBox="0 0 20 20" aria-label="email"><rect x="1" y="4" width="18" height="12" fill="var(--periwinkle)"/><path d="M1 4l9 7 9-7" fill="none" stroke="#050505" stroke-width="1.5"/></svg>
    <svg viewBox="0 0 20 20" aria-label="website"><circle cx="10" cy="10" r="8" fill="none" stroke="var(--periwinkle)" stroke-width="1.6"/><ellipse cx="10" cy="10" rx="3.5" ry="8" fill="none" stroke="var(--periwinkle)" stroke-width="1.2"/><path d="M2 10h16M3.5 6h13M3.5 14h13" stroke="var(--periwinkle)" stroke-width="1.2"/></svg>
  </div>

  <div class="contact-list">
    <div>555 -0142- 078</div>
    <div>hello@lunarpathstudio.com</div>
    <div>www.lunarpathstudio.com</div>
  </div>

  <div class="social-list">
    <div>social.example/LunarPathStudio</div>
    <div>gather.example/Lunar-Path-Studio</div>
  </div>
</section>

<section class="card card--back">
  <div class="brand-name">Lunar Path<br>Studio</div>

  <div class="services">
    <span class="row row--ruled"><span>Tantra<i class="dot"></i>Tao<i class="dot"></i>Yaga<i class="dot"></i>Tai Chi<i class="dot"></i>Reiki</span></span>
    <span class="row">Sacred Sexuality<i class="dot"></i>Sexual Healing<i class="dot"></i>Sound Healing</span>
    <span class="row row--ruled"><span>Energy Work<i class="dot"></i>Rituals</span></span>
    <span class="row">Partners Yoga<i class="dot"></i>Four Hand Massage</span>
  </div>

  <div class="punch-grid">
    <div class="punch"><svg viewBox="0 0 108 108" role="img" aria-label="ornamental mandala punch badge"><circle cx="54" cy="54" r="52" fill="var(--cream)"/><circle cx="54" cy="54" r="38" fill="var(--periwinkle)"/></svg><span class="punch__value">180$</span></div>
    <div class="punch"><svg viewBox="0 0 108 108" role="img" aria-label="ornamental mandala punch badge"><circle cx="54" cy="54" r="52" fill="var(--cream)"/><circle cx="54" cy="54" r="38" fill="var(--periwinkle)"/></svg><span class="punch__value">180$</span></div>
    <div class="punch"><svg viewBox="0 0 108 108" role="img" aria-label="ornamental mandala punch badge"><circle cx="54" cy="54" r="52" fill="var(--cream)"/><circle cx="54" cy="54" r="38" fill="var(--periwinkle)"/></svg><span class="punch__value">180$</span></div>
    <div class="punch"><svg viewBox="0 0 108 108" role="img" aria-label="ornamental mandala punch badge"><circle cx="54" cy="54" r="52" fill="var(--cream)"/><circle cx="54" cy="54" r="38" fill="var(--periwinkle)"/></svg><span class="punch__value">180$</span></div>
    <div class="punch"><svg viewBox="0 0 108 108" role="img" aria-label="ornamental mandala punch badge"><circle cx="54" cy="54" r="52" fill="var(--cream)"/><circle cx="54" cy="54" r="38" fill="var(--periwinkle)"/></svg><span class="punch__value">180$</span></div>
    <div class="punch"><svg viewBox="0 0 108 108" role="img" aria-label="ornamental mandala punch badge"><circle cx="54" cy="54" r="52" fill="var(--cream)"/><circle cx="54" cy="54" r="38" fill="var(--periwinkle)"/></svg><span class="punch__value">180$</span></div>
    <div class="punch"><svg viewBox="0 0 108 108" role="img" aria-label="ornamental mandala punch badge"><circle cx="54" cy="54" r="52" fill="var(--cream)"/><circle cx="54" cy="54" r="38" fill="var(--periwinkle)"/></svg><span class="punch__value">180$</span></div>
    <div class="punch"><svg viewBox="0 0 108 108" role="img" aria-label="ornamental mandala punch badge"><circle cx="54" cy="54" r="52" fill="var(--cream)"/><circle cx="54" cy="54" r="38" fill="var(--periwinkle)"/></svg><span class="punch__value">180$</span></div>
    <div class="punch"><svg viewBox="0 0 108 108" role="img" aria-label="ornamental mandala punch badge"><circle cx="54" cy="54" r="52" fill="var(--cream)"/><circle cx="54" cy="54" r="38" fill="var(--periwinkle)"/></svg><span class="punch__value">180$</span></div>
  </div>
</section>

</body>
</html>
```